Bright Wave Labs

We need a professional letter head format for our company. Now we have a logo but need to desing a new logo also. I have uploaded our old logo. Use the color in the logo and design a new one.

Dear Designers , Need to mention "BWL" and please dont use our old LOGO. we need a new catchy one.

```html
<!DOCTYPE html>
<html lang="en">
<head>
<meta charset="utf-8">
<title>Bright Wave Labs — Letterhead</title>
<link rel="stylesheet" href="https://fonts.googleapis.com/css2?family=Open+Sans:wght@400;600;700&display=swap">
<style>
  :root {
    --navy: #0f2d4a;
    --green: #8cc63f;
    --ink: #3a3a3a;
    --ink-soft: #555b61;
    --paper: #ffffff;
    --paper-shade: #eef0f2;
    --backdrop: #e6e7e9;
  }
  * { box-sizing: border-box; margin: 0; padding: 0; }
  html, body { width: 1200px; height: 1120px; overflow: hidden; }
  body {
    background: var(--backdrop);
    font-family: "Open Sans", Arial, sans-serif;
    color: var(--ink);
  }
  .letterhead {
    position: absolute;
    left: 232px; top: 40px;
    width: 736px; height: 1040px;
    background: linear-gradient(135deg, var(--paper) 45%, var(--paper-shade) 100%);
    box-shadow: 0 6px 24px rgba(0,0,0,0.12);
    overflow: hidden;
  }
  .brand {
    position: absolute; left: 56px; top: 52px;
    display: flex; align-items: center; gap: 10px;
  }
  .brand-dot { width: 22px; height: 22px; border-radius: 50%; background: var(--green); }
  .brand-name {
    font-size: 19px; font-weight: 700; color: var(--navy);
    letter-spacing: 0.02em; text-transform: uppercase;
  }
  .contact {
    position: absolute; right: 56px; top: 50px;
    list-style: none; font-size: 10.5px; line-height: 17px; color: var(--ink-soft);
  }
  .contact li { display: flex; align-items: center; gap: 6px; }
  .contact svg { width: 10px; height: 10px; fill: var(--green); }
  .letter-body { position: absolute; left: 90px; top: 150px; width: 520px; }
  .salutation { font-size: 15px; font-weight: 700; color: var(--ink); margin-bottom: 18px; }
  .letter-body p { font-size: 11.5px; line-height: 18px; color: var(--ink-soft); margin-bottom: 22px; }
  .signature {
    width: 130px; height: 80px; margin-top: 30px;
    background: linear-gradient(90deg, #e4e6e8, #f1f2f3);
    border-radius: 4px;
  }
  .footer-band {
    position: absolute; left: 0; bottom: 0; width: 100%; height: 40px;
    background: var(--navy); color: #fff;
    display: flex; align-items: center; padding-left: 28px; gap: 8px;
    font-size: 11px;
  }
  .footer-band svg { width: 11px; height: 14px; fill: #fff; }
  .web-tab {
    position: absolute; right: 0; bottom: 40px;
    width: 250px; height: 28px;
    background: var(--green); color: #fff;
    border-top-left-radius: 18px;
    display: flex; align-items: center; justify-content: center;
    font-size: 11px; font-weight: 600;
  }
</style>
</head>
<body>
  <main class="letterhead">
    <header class="brand">
      <span class="brand-dot"></span>
      <span class="brand-name">Bright Wave Labs</span>
    </header>

    <ul class="contact">
      <li><svg viewBox="0 0 10 10"><path d="M2 0l2 2-1 1.5c.6 1.3 1.6 2.3 2.9 2.9L7.4 5.4 9.5 7.5 8 9.5C4 9.5.5 6 .5 2z"/></svg>+1 (555) 010-2040</li>
      <li><svg viewBox="0 0 10 10"><rect x="0" y="2" width="10" height="6" rx="1"/></svg>+1 (555) 010-3050</li>
      <li><svg viewBox="0 0 10 10"><path d="M0 2h10v6H0z M0 2l5 3.5L10 2" /></svg>info@brightwavelabs.com</li>
    </ul>

    <section class="letter-body">
      <h1 class="salutation">Dear Mr. John,</h1>
      <p>Lorem Ipsum is simply dummy text of the printing and typesetting industry. Lorem Ipsum has been the industry's standard dummy text ever since the 1500s, when an unknown printer took a galley of type and scrambled it to make a type specimen book. It has survived not only five centuries, but also the leap into electronic typesetting, remaining essentially unchanged.</p>
      <p>The standard chunk of Lorem Ipsum used since the 1500s is reproduced below for those interested. Sections 1.10.32 and 1.10.33 from "On the Measure of Good Things" by Marcus Veldren are also reproduced in their exact original form, accompanied by English versions from the 1914 translation by H. Calloway.</p>
      <p>Lorem Ipsum is simply dummy text of the printing and typesetting industry. Lorem Ipsum has been the industry's standard dummy text ever since the 1500s, when an unknown printer took a galley of type and scrambled it to make a type specimen book. It has survived not only five centuries, but also the leap into electronic typesetting, remaining essentially unchanged. It was popularised in the</p>
      <p>Lorem Ipsum is simply dummy text of the printing and typesetting industry. Lorem Ipsum has been the industry's standard dummy text ever since the 1500s, when an unknown printer took a galley of type and scrambled it to make a type specimen book. It has survived not only five centuries, but also the leap into electronic typesetting, remaining essentially unchanged. It was popularised in the</p>
      <div class="signature" role="img" aria-label="Handwritten signature of the sender"></div>
    </section>

    <div class="web-tab">www.brightwavelabs.com</div>
    <footer class="footer-band">
      <svg viewBox="0 0 11 14"><path d="M5.5 0A5 5 0 0 0 .5 5c0 3.5 5 9 5 9s5-5.5 5-9a5 5 0 0 0-5-5zm0 7a2 2 0 1 1 0-4 2 2 0 0 1 0 4z"/></svg>
      <span>PO Box 418, Harbor Lane, Eastfield, Zip Code 20410</span>
    </footer>
  </main>
</body>
</html>
```